Stonelynk Business Card Design

The Stonelynk Co is an aggregate (crushing) equipment dealer serving Western Canadian provinces. Stonelynk is a distributor of aggregate equipment for different manufacturers.

We are looking to change and update the existing business card which has been used since the existence of the company. A copy of existing card has been attached for reference. The Stonelynk Co logo we want to remain the same and we want the green color to remain the same.

We are wanting something new with a different look. A refreshing card to show a new modern and updated look. No longer wanting to have the manufacturers on the back of the card but something more like our logo on the back of the card with a statement like "Crushing Solutions"

ideas could be:
- card can be different colors on front and back
- front or reverse of the card could possibly be the green color with the logo in black

Target Market(s)

Owners of Aggregate/Crushing companies

Requirements
Must have
• - logo to remain same along with same font within logo
• - green color to remain same
Nice to have
• as noted above under project description
Should not have

```html
<!DOCTYPE html>
<html lang="en">
<head>
<meta charset="utf-8">
<title>The Stonelynk Co – Business Card</title>
<link href="https://fonts.googleapis.com/css2?family=Arimo:wght@400;700&display=swap" rel="stylesheet">
<style>
  :root {
    --backdrop: #b9b9b9;
    --brand-green: #8a8c0a;
    --card-charcoal: #231f20;
    --ink-white: #ffffff;
    --ink-soft: #e6e6e6;
  }
  * { margin: 0; padding: 0; box-sizing: border-box; }
  html, body {
    width: 1200px; height: 900px; overflow: hidden;
    background: var(--backdrop);
    font-family: "Arimo", Arial, sans-serif;
  }
  .canvas { position: relative; width: 1200px; height: 900px; }

  .card { position: absolute; top: 275px; width: 479px; height: 295px; color: var(--ink-white); }
  .card--front {
    left: 116px; background: var(--brand-green);
    border-radius: 0 48px 0 48px;
  }
  .card--back {
    left: 622px; background: var(--card-charcoal);
    border-radius: 48px 0 48px 0;
  }

  .wordmark { position: absolute; font-weight: 700; font-size: 21px; letter-spacing: 0.2px; white-space: nowrap; }
  .card--front .wordmark { right: 28px; top: 116px; }
  .card--back .wordmark { left: 0; right: 0; text-align: center; top: 174px; color: var(--ink-soft); }

  .brand-dot { position: absolute; border-radius: 50%; }
  .card--front .brand-dot { right: 80px; top: 44px; width: 52px; height: 52px; background: var(--ink-white); }
  .card--back .brand-dot { left: 213px; top: 103px; width: 52px; height: 52px; background: var(--brand-green); }

  .person-name {
    position: absolute; left: 21px; right: 28px; top: 160px;
    display: flex; align-items: center; gap: 8px;
    font-size: 18.5px; white-space: nowrap;
  }
  .person-name .rule { flex: 1; height: 1px; background: var(--ink-white); }

  .contact-list { position: absolute; list-style: none; font-size: 14px; line-height: 17.5px; }
  .contact-list li { display: flex; align-items: center; gap: 6px; white-space: nowrap; }
  .contact-list svg { width: 11px; height: 11px; fill: var(--ink-white); flex: none; }
  .phones { left: 21px; top: 212px; }
  .links { right: 28px; top: 187px; text-align: right; }
  .links li { justify-content: flex-end; }
  .address { position: absolute; right: 28px; top: 230px; text-align: right; font-size: 14px; line-height: 17.5px; font-style: normal; }

  .tagline {
    position: absolute; left: 0; right: 0; top: 226px; text-align: center;
    font-weight: 700; font-size: 14px; letter-spacing: 1.6px; color: var(--ink-soft);
  }
</style>
</head>
<body>
<main class="canvas">
  <section class="card card--front" aria-label="Card front">
    <span class="brand-dot" aria-hidden="true"></span>
    <div class="wordmark">THE STONELYNK CO.</div>

    <div class="person-name"><span>DALE VARRICK</span><span class="rule"></span></div>

    <ul class="contact-list links">
      <li>dale@stonel.com
        <svg viewBox="0 0 12 12"><path d="M1 3h10v7H1z M1 3l5 4 5-4" fill="none" stroke="#fff" stroke-width="1.2"/></svg></li>
      <li>www.stonelynk.ca
        <svg viewBox="0 0 12 12"><circle cx="6" cy="6" r="5.5"/><path d="M6 .5v11M.5 6h11M6 .5c-3 3-3 8 0 11M6 .5c3 3 3 8 0 11" fill="none" stroke="#8a8c0a" stroke-width="0.9"/></svg></li>
    </ul>

    <ul class="contact-list phones">
      <li><svg viewBox="0 0 12 12"><path d="M1 4c0-2 10-2 10 0v1H8V4H4v1H1z M3 6h6l1 4H2z"/></svg>780.555.0142(Direct)</li>
      <li><svg viewBox="0 0 12 12"><path d="M1 4c0-2 10-2 10 0v1H8V4H4v1H1z M3 6h6l1 4H2z"/></svg>780.555.0187</li>
      <li><svg viewBox="0 0 12 12"><path d="M3 1h5v3H3z M1 4h10v7H1z" /><rect x="3" y="6" width="6" height="3" fill="#8a8c0a"/></svg>780.555.0163</li>
    </ul>

    <address class="address">2218-47B Avenue<br>Brookvale, Alberta T0X 1R2</address>
  </section>

  <section class="card card--back" aria-label="Card back">
    <span class="brand-dot" aria-hidden="true"></span>
    <div class="wordmark">THE STONELYNK CO.</div>
    <p class="tagline">CRUSHING SOLUTIONS</p>
  </section>
</main>
</body>
</html>
```